Design door hanger Bonaire Diving

We would like to have a design for a door hanger (See example below).
One side: Promote reef taster diving.
Other side: Promote Unlimited air/nitrox packages - lowest price guaranteed on Bonaire

We would like to inform people who rent a car with us about our air packages for diving. And non divers should be triggered to come and do a Reef Taster Dive with us. (KT Car rental and KT Dive is the same company.)

Target Market(s)

Divers and potential divers

Industry/Entity Type

Diving industry

Font styles to use
Sans Serif

Colors
0054AA
0677BA
7BADD7
CADEEF
E8F1F8
EE7325
F08F49
F5BC92
FAE3D3
FDF4ED

Requirements
Must have
• a few of the pictures included

```html
<!DOCTYPE html>
<html lang="en">
<head>
<meta charset="utf-8">
<title>KT Car Rental &amp; KT Dive – Door Hangers</title>
<link rel="stylesheet" href="https://fonts.googleapis.com/css2?family=Poppins:wght@400;500;600;700;800&display=swap">
<style>
  :root {
    --page: #dcdcdc;
    --navy: #0f3360;
    --navy-deep: #0b2a52;
    --orange: #f4a62a;
    --ink: #0f2f5a;
    --white: #ffffff;
    --panel: rgba(90, 130, 170, 0.28);
  }
  * { box-sizing: border-box; margin: 0; padding: 0; }
  html, body { width: 867px; height: 1200px; overflow: hidden; background: var(--page); }
  body { font-family: "Poppins", sans-serif; color: var(--white); position: relative; }

  .hanger { position: absolute; top: 147px; width: 329px; height: 847px; }
  .hanger--reef { left: 58px; }
  .hanger--air { left: 481px; }
  .hanger__shape { position: absolute; inset: 0; width: 329px; height: 847px; }
  .hanger__content { position: absolute; inset: 0; }

  .brand { position: absolute; top: 330px; left: 0; width: 329px; text-align: center;
           font-weight: 700; font-size: 25px; line-height: 1.15; color: var(--white); }

  .headline { position: absolute; left: 0; width: 329px; text-align: center; font-weight: 800; line-height: 1; }
  .headline--reef-top { top: 425px; font-size: 33px; color: var(--orange); }
  .headline--reef-bottom { top: 460px; font-size: 35px; color: var(--white); }
  .rule { position: absolute; top: 500px; left: 112px; width: 104px; height: 2px; background: var(--orange); }

  .intro { position: absolute; top: 507px; left: 20px; width: 289px; font-size: 8.3px; line-height: 1.25; text-align: center; }

  .perks { position: absolute; top: 540px; list-style: none; font-size: 8px; line-height: 1.22; }
  .perks--left { left: 12px; width: 148px; }
  .perks--right { left: 166px; width: 150px; }
  .perks li { position: relative; padding-left: 11px; margin-bottom: 5px; }
  .perks li::before { content: ""; position: absolute; left: 0; top: 2px; width: 6px; height: 6px; border-radius: 50%; background: var(--orange); }

  .cta { position: absolute; left: 47px; width: 228px; height: 28px; border-radius: 5px; background: var(--orange); color: var(--ink);
         display: flex; align-items: center; justify-content: center; gap: 6px; font-weight: 700; font-size: 13.5px; white-space: nowrap; }
  .cta svg { width: 14px; height: 14px; }
  .cta--reef { top: 612px; }
  .cta--air { top: 620px; }
  .site { position: absolute; left: 0; width: 329px; text-align: center; font-weight: 500; font-size: 12px; letter-spacing: 3.6px; }
  .site--reef { top: 645px; }
  .site--air { top: 653px; }

  .headline--air-top { top: 420px; font-size: 44px; color: var(--orange); }
  .sub { position: absolute; left: 0; width: 329px; text-align: center; font-weight: 700; font-size: 18.5px; line-height: 1; }
  .sub--white { top: 465px; color: var(--white); }
  .sub--orange { top: 487px; color: var(--orange); }

  .offer { position: absolute; top: 514px; left: 13px; width: 303px; height: 49px; border-radius: 7px; background: var(--panel); display: flex; overflow: hidden; }
  .offer__label { width: 78px; padding: 6px 0 0 8px; font-weight: 700; font-size: 14.5px; line-height: 1.05; color: var(--orange); border-right: 3px solid var(--navy-deep); }
  .offer__text { flex: 1; padding: 7px 8px; font-weight: 600; font-size: 11.5px; line-height: 1.25; }

  .fill { position: absolute; top: 570px; left: 0; width: 329px; text-align: center; font-size: 14px; line-height: 1.25; }
  .fill strong { color: var(--orange); font-weight: 700; }
</style>
</head>
<body>

<section class="hanger hanger--reef" aria-label="Reef Taster Dive door hanger">
  <svg class="hanger__shape" viewBox="0 0 329 847">
    <defs>
      <clipPath id="cut-reef">
        <path d="M0 165 A165 165 0 0 1 329 165 L329 807 Q329 847 289 847 L40 847 Q0 847 0 807 L0 330 Q0 288 60 282 C160 262 250 240 262 205 A104 104 0 1 0 64 195 A34 34 0 0 1 0 170 Z"/>
      </clipPath>
      <linearGradient id="sea-reef" x1="0" y1="0" x2="0" y2="1">
        <stop offset="0" stop-color="#143f70"/>
        <stop offset="0.5" stop-color="#0f3360"/>
        <stop offset="1" stop-color="#0f3360"/>
      </linearGradient>
      <linearGradient id="photo-reef" x1="0" y1="0" x2="0" y2="1">
        <stop offset="0" stop-color="#0f3360"/>
        <stop offset="0.3" stop-color="#1b5f8c"/>
        <stop offset="0.75" stop-color="#2f7f8e"/>
        <stop offset="1" stop-color="#6e8a7a"/>
      </linearGradient>
    </defs>
    <g clip-path="url(#cut-reef)">
      <rect width="329" height="847" fill="url(#sea-reef)"/>
      <rect y="660" width="329" height="187" fill="url(#photo-reef)" role="img" aria-label="Photo of a sea turtle swimming above a coral reef"/>
    </g>
  </svg>
  <div class="hanger__content">
    <p class="brand">KT CAR RENTAL<br>&amp; KT DIVE</p>
    <h1 class="headline headline--reef-top">REEF TASTER</h1>
    <h2 class="headline headline--reef-bottom">DIVING</h2>
    <div class="rule"></div>
    <p class="intro">Dive for the first time and enjoy our underwater paradise to the fullest under the guidance of an instructor. Give yourself a lifetime gift.</p>
    <ul class="perks perks--left">
      <li>Ages 10 and up can sign up for our reef taster dive</li>
      <li>The Reef Taster Diving course will take 3-4 hours</li>
      <li>A group consists of a maximum of 4 people</li>
    </ul>
    <ul class="perks perks--right">
      <li>Experience the splendor of the ocean without much distraction by other divers</li>
      <li>Enjoy a lot of personal attention given by your instructor</li>
    </ul>
    <div class="cta cta--reef">CALL NOW
      <svg viewBox="0 0 24 24" aria-hidden="true"><path fill="#0f2f5a" d="M6.6 10.8a15 15 0 0 0 6.6 6.6l2.2-2.2c.3-.3.7-.4 1-.2 1.1.4 2.3.6 3.6.6.6 0 1 .4 1 1V20c0 .6-.4 1-1 1A17 17 0 0 1 3 4c0-.6.4-1 1-1h3.5c.6 0 1 .4 1 1 0 1.3.2 2.5.6 3.6.1.3 0 .7-.2 1z"/></svg>
      +599-555-0142</div>
    <p class="site site--reef">www.ktcarrental.com</p>
  </div>
</section>

<section class="hanger hanger--air" aria-label="Unlimited air door hanger">
  <svg class="hanger__shape" viewBox="0 0 329 847">
    <defs>
      <clipPath id="cut-air">
        <path d="M0 165 A165 165 0 0 1 329 165 L329 807 Q329 847 289 847 L40 847 Q0 847 0 807 L0 330 Q0 288 60 282 C160 262 250 240 262 205 A104 104 0 1 0 64 195 A34 34 0 0 1 0 170 Z"/>
      </clipPath>
      <linearGradient id="sea-air" x1="0" y1="0" x2="0" y2="1">
        <stop offset="0" stop-color="#143f70"/>
        <stop offset="0.5" stop-color="#0f3360"/>
        <stop offset="1" stop-color="#0f3360"/>
      </linearGradient>
      <linearGradient id="photo-air" x1="0" y1="0" x2="0" y2="1">
        <stop offset="0" stop-color="#0f3360"/>
        <stop offset="0.35" stop-color="#1f6a80"/>
        <stop offset="0.75" stop-color="#2c5f68"/>
        <stop offset="1" stop-color="#8a8a72"/>
      </linearGradient>
    </defs>
    <g clip-path="url(#cut-air)">
      <rect width="329" height="847" fill="url(#sea-air)"/>
      <rect y="670" width="329" height="177" fill="url(#photo-air)" role="img" aria-label="Photo of a reef fish beside dive tanks and gear resting on rocks"/>
    </g>
  </svg>
  <div class="hanger__content">
    <p class="brand">KT CAR RENTAL<br>&amp; KT DIVE</p>
    <h1 class="headline headline--air-top">UNLIMITED</h1>
    <p class="sub sub--white">SUSTAINABLE AIR</p>
    <p class="sub sub--orange">AT A COMPETITIVE RATE</p>
    <div class="offer">
      <p class="offer__label">KT-DIVE OFFERS</p>
      <p class="offer__text">Unlimited air/nitrox for the lowest price on Bonaire</p>
    </div>
    <p class="fill">We fill your tank up to <strong>3200 PSI (220 BAR)</strong><br>without problem</p>
    <div class="cta cta--air">CALL NOW
      <svg viewBox="0 0 24 24" aria-hidden="true"><path fill="#0f2f5a" d="M6.6 10.8a15 15 0 0 0 6.6 6.6l2.2-2.2c.3-.3.7-.4 1-.2 1.1.4 2.3.6 3.6.6.6 0 1 .4 1 1V20c0 .6-.4 1-1 1A17 17 0 0 1 3 4c0-.6.4-1 1-1h3.5c.6 0 1 .4 1 1 0 1.3.2 2.5.6 3.6.1.3 0 .7-.2 1z"/></svg>
      +599-555-0142</div>
    <p class="site site--air">www.ktcarrental.com</p>
  </div>
</section>

</body>
</html>
```